Letterhead for a German Distribution/Manufacturing Company

We need a professional Letterhead in a unique Design.
not to playful.
The Letterhead has to show show that we are a international company with headquater in Germany.
all details like adress, Vat Tax Number, Bank Accout, Eori, email, Company number has to be on the Letterhead.
for example use: VAT TAX DE5704168 Bank Account: Norrfeld Bank IBAN DE421705238ß310482 Swift: KOLV3154802 EORI 3041296587 Company Number: HRB 61508 Adress: VOLTRINA UG Amsel Strasse 7 Postal Code 04683 City Velmstadt Country: Germany Email: info@voltrina-example.com
the design can be colored but doesnt have to be
Industry/Entity Type
Manufacturing and international distribution
Requirements
Must have
- show that we are a international company with headquater in Germany. our company infos and logo

```html
<!DOCTYPE html>
<html lang="en">
<head>
<meta charset="utf-8">
<title>VOLTRINA Letterhead</title>
<link rel="stylesheet" href="https://fonts.googleapis.com/css2?family=Nunito+Sans:wght@400;600;700&display=swap">
<style>
  :root {
    --canvas: #e2e2e2;
    --paper: #ffffff;
    --ink: #222222;
    --heading: #3a3a3a;
    --brand: #555555;
    --muted: #6b6b6b;
    --footer: #555555;
    --swoosh: #b3b3b3;
    --footer-text: #ffffff;
    --sig-fill: #f1f1f1;
  }
  html, body {
    margin: 0;
    padding: 0;
    width: 1200px;
    height: 1200px;
    overflow: hidden;
    background: var(--canvas);
    font-family: "Nunito Sans", sans-serif;
  }
  .letterhead {
    position: absolute;
    left: 216px;
    top: 76px;
    width: 768px;
    height: 1046px;
    background: var(--paper);
    overflow: hidden;
  }
  .brand {
    position: absolute;
    top: 54px;
    left: 0;
    right: 0;
    text-align: center;
    font-size: 58px;
    font-weight: 600;
    color: var(--brand);
    letter-spacing: 1px;
    line-height: 70px;
  }
  .greeting {
    position: absolute;
    left: 54px;
    top: 258px;
    margin: 0;
    font-size: 23.5px;
    font-weight: 700;
    color: var(--heading);
  }
  .body-copy {
    position: absolute;
    left: 55px;
    top: 304px;
    width: 659px;
    color: var(--ink);
    font-size: 18.6px;
    line-height: 21.3px;
    letter-spacing: -0.1px;
  }
  .body-copy p {
    margin: 0 0 21.3px;
    text-align: justify;
  }
  .signatory {
    position: absolute;
    left: 63px;
    top: 767px;
    color: var(--muted);
  }
  .signatory .name { font-size: 11px; line-height: 14px; }
  .signatory .role { font-size: 8.5px; line-height: 12px; }
  .signature-mark {
    position: absolute;
    left: 55px;
    top: 790px;
    width: 170px;
    height: 84px;
    background: radial-gradient(ellipse at center, var(--sig-fill) 0%, rgba(255,255,255,0) 75%);
  }
  .footer-wave {
    position: absolute;
    left: 0;
    top: 890px;
    width: 768px;
    height: 156px;
  }
  .footer-contact, .footer-legal {
    position: absolute;
    color: var(--footer-text);
    font-size: 10.6px;
    line-height: 13.3px;
  }
  .footer-contact { left: 122px; top: 978px; }
  .footer-contact .row { display: flex; align-items: flex-start; gap: 7px; margin-bottom: 2.7px; }
  .footer-contact svg { width: 12px; height: 12px; flex: none; margin-top: 1px; }
  .footer-divider {
    position: absolute;
    left: 347px;
    top: 983px;
    width: 1px;
    height: 54px;
    background: rgba(255,255,255,0.45);
  }
  .footer-legal { left: 388px; top: 982px; }
</style>
</head>
<body>
  <main class="letterhead">
    <div class="brand">VOLTRINA</div>

    <h1 class="greeting">Dear Mr. John,</h1>

    <section class="body-copy">
      <p>Lorem ipsum dolor sit amet, consectetuer adipiscing elit, sed diam nonummy nibh euismod tincidunt ut laoreet dolore magna aliquam erat volutpat. Ut wisi enim ad minim veniam, quis nostrud exerci tation ullamcorper suscipit lobortis nisl ut aliquip ex ea commodo consequat. Duis autem vel eum iriure dolor in<br>&nbsp;hendrerit in vulputate velit esse molestie consequat, vel illum dolore eu feugiat nulla facilisis at vero eros et accumsan et iusto odio dignissim qui blandit praesent luptatum zzril delenit augue duis dolore te feugait nulla facilisi.</p>
      <p>Lorem ipsum dolor sit amet, cons ectetuer adipiscing elit, sed diam nonummy nibh euismod tincidunt ut laoreet dolore magna aliquam erat volutpat. Ut wisi Lorem ipsum dolor sit amet, consectetuer adipiscing elit, sed diam nonummy nibh euismod tincidunt ut laoreet dolore magna aliquam erat volutpat. Ut wisi enim ad minim veniam, quis nostrud exerci tation ullamcorper suscipit lobortis nisl ut aliquip ex ea commodo consequat. Duis autem vel eum iriure dolor in hendrerit in vulputate velit esse molestie consequat,Lorem ipsum dolor sit amet, cons ectetuer adipiscing elit, sed diam nonummy nibh euismod tincidunt ut laoreet dolore magna aliquam erat volutpat.</p>
    </section>

    <div class="signatory">
      <div class="name">John Doe</div>
      <div class="role">Office Maneger</div>
    </div>
    <div class="signature-mark" role="img" aria-label="Handwritten signature"></div>

    <svg class="footer-wave" viewBox="0 0 768 156" aria-hidden="true">
      <path d="M0 42 Q330 118 768 6 L768 32 Q330 132 0 46 Z" fill="var(--swoosh)"/>
      <path d="M0 46 Q330 132 768 32 L768 156 L0 156 Z" fill="var(--footer)"/>
    </svg>

    <div class="footer-contact">
      <div class="row">
        <svg viewBox="0 0 12 12" aria-hidden="true"><circle cx="6" cy="6" r="5" fill="none" stroke="#fff" stroke-width="1"/><ellipse cx="6" cy="6" rx="2.2" ry="5" fill="none" stroke="#fff" stroke-width="0.9"/><line x1="1" y1="6" x2="11" y2="6" stroke="#fff" stroke-width="0.9"/></svg>
        <span>www.voltrina-example.com</span>
      </div>
      <div class="row">
        <svg viewBox="0 0 12 12" aria-hidden="true"><rect x="0.5" y="2.5" width="11" height="7.5" fill="#fff"/><path d="M0.5 2.5 L6 7 L11.5 2.5" fill="none" stroke="var(--footer)" stroke-width="1"/></svg>
        <span>info@voltrina-example.com</span>
      </div>
      <div class="row">
        <svg viewBox="0 0 12 12" aria-hidden="true"><path d="M6 11.5 C3 8 2 6.3 2 4.5 A4 4 0 0 1 10 4.5 C10 6.3 9 8 6 11.5 Z" fill="none" stroke="#fff" stroke-width="1.3"/><circle cx="6" cy="4.5" r="1.4" fill="#fff"/></svg>
        <span>VOLTRINA UG | Amsel Strasse 7<br>04683 Velmstadt,Germany</span>
      </div>
    </div>

    <div class="footer-divider"></div>

    <div class="footer-legal">
      VAT TAX DE5704168<br>
      Bank Account: Norrfeld Bank IBAN DE421705238ß310482<br>
      Swift: KOLV3154802 EORI 3041296587<br>
      Company Number: HRB 61508
    </div>
  </main>
</body>
</html>
```